Acupuncture business needs business card design

I need a business card for an acupuncture clinic called "Summit Wellpath"
It will need the following details:
My name: Marcus Thelwick
Acupuncturist
Member KPTG
BVF Treatment Provider
Ph numbers: 482 1358 027 514 3820
Email: marcus@swpath.example.nz
On the back it will need a table with 2 columns for appointments, one column for time and one for date.

Industry/Entity Type

Clinic

Contact Information for Business Card

Marcus Thelwick
Acupuncturist
Member KPTG
BVF Treatment Provider
Email: marcus@swpath.example.nz

Requirements
Must have
• Marcus Thelwick
• Acupuncturist
• Member KPTG
• BVF Treatment Provider
• Ph numbers: 482 1358 027 514 3820
• Email: marcus@swpath.example.nz
• On the back it will need a table with 2 columns for appointments, one column for time and one for date.

```html
<!DOCTYPE html>
<html lang="en">
<head>
<meta charset="utf-8">
<title>Summit Wellpath – Business Card</title>
<link rel="stylesheet" href="https://fonts.googleapis.com/css2?family=Source+Sans+3:wght@400;600&display=swap">
<style>
  :root {
    --page: #e8e4d8;
    --brand-blue: #27a8de;
    --deep-blue: #1479a8;
    --card-white: #ffffff;
    --card-black: #0b0b0c;
    --ink: #2b2b2b;
    --field-line: #8a8a8a;
    --muted-white: #e6e6e6;
  }
  * { box-sizing: border-box; margin: 0; padding: 0; }
  html, body {
    width: 1200px; height: 978px; overflow: hidden;
    background: var(--page);
    font-family: "Source Sans 3", "Myriad Pro", sans-serif;
  }
  .canvas { position: relative; width: 1200px; height: 978px; }

  .card {
    position: absolute; left: 220px; width: 760px; height: 434px;
    border-radius: 26px; overflow: hidden;
    box-shadow: 0 6px 18px rgba(0,0,0,.18);
  }
  .card--back { top: 30px; background: var(--card-white); }
  .card--front { top: 514px; background: var(--card-black); }

  /* brand lockup */
  .brand { position: absolute; display: flex; align-items: center; gap: 16px; }
  .brand__dot {
    width: 50px; height: 50px; border-radius: 50%;
    background: var(--brand-blue); flex: none;
  }
  .brand__text { display: flex; flex-direction: column; }
  .brand__name {
    font-weight: 600; font-size: 50px; line-height: 1;
    color: var(--brand-blue); letter-spacing: -.5px;
  }
  .brand__tagline {
    font-weight: 400; font-size: 15px; letter-spacing: 4.6px;
    color: var(--brand-blue); text-transform: uppercase; margin-top: 4px;
  }
  .card--back .brand { left: 74px; top: 46px; }
  .card--front .brand { left: 250px; top: 58px; }

  /* appointment table */
  .appointment {
    position: absolute; left: 100px; top: 168px; width: 560px;
    display: grid; grid-template-columns: 74px 1fr; row-gap: 20px;
    align-items: center;
  }
  .appointment__label { font-size: 27px; color: var(--ink); }
  .appointment__field {
    height: 38px; border: 1.5px solid var(--field-line);
    box-shadow: inset 1px 1px 2px rgba(0,0,0,.12);
  }
  .appointment__date { display: grid; grid-template-columns: 1fr 70px 1fr; gap: 8px; }
  .website {
    position: absolute; left: 0; right: 0; top: 330px;
    text-align: center; font-size: 27px; letter-spacing: 4px; color: var(--ink);
  }

  /* front details */
  .waves { position: absolute; inset: 0; width: 760px; height: 434px; }
  .practitioner {
    position: absolute; left: 40px; top: 178px; width: 300px;
    text-align: right; color: var(--brand-blue);
  }
  .practitioner__name { font-weight: 600; font-size: 24px; }
  .practitioner__role { font-size: 18px; line-height: 1.3; }
  .divider {
    position: absolute; left: 362px; top: 180px; width: 1px; height: 96px;
    background: var(--muted-white); opacity: .7;
  }
  .contact {
    position: absolute; left: 388px; top: 190px;
    display: flex; flex-direction: column; gap: 18px;
    color: var(--muted-white); font-size: 21px;
  }
  .contact__row { display: flex; align-items: center; gap: 12px; }
  .contact__icon { width: 22px; height: 22px; flex: none; }
</style>
</head>
<body>
<main class="canvas">

  <section class="card card--back" aria-label="Card back – appointment card">
    <div class="brand">
      <span class="brand__dot"></span>
      <div class="brand__text">
        <span class="brand__name">Summit Wellpath</span>
        <span class="brand__tagline">Acupuncture Physiotherapy</span>
      </div>
    </div>
    <div class="appointment">
      <span class="appointment__label">Time</span>
      <span class="appointment__field"></span>
      <span class="appointment__label">Date</span>
      <div class="appointment__date">
        <span class="appointment__field"></span>
        <span class="appointment__field"></span>
        <span class="appointment__field"></span>
      </div>
    </div>
    <p class="website">www.swpath.example.nz</p>
  </section>

  <section class="card card--front" aria-label="Card front – contact details">
    <svg class="waves" viewBox="0 0 760 434" aria-hidden="true">
      <path d="M0 250 C120 300 230 350 360 434 L0 434 Z" fill="#0d4f6e"/>
      <path d="M0 275 C130 320 250 370 330 434 L0 434 Z" fill="var(--brand-blue)"/>
      <path d="M0 305 C120 345 200 390 260 434 L0 434 Z" fill="#0b0b0c"/>
      <path d="M0 325 C110 360 180 400 225 434 L0 434 Z" fill="var(--deep-blue)"/>
      <path d="M0 350 C90 380 150 410 180 434 L0 434 Z" fill="var(--brand-blue)"/>
    </svg>

    <div class="brand">
      <span class="brand__dot"></span>
      <div class="brand__text">
        <span class="brand__name">Summit Wellpath</span>
        <span class="brand__tagline">Acupuncture Physiotherapy</span>
      </div>
    </div>

    <div class="practitioner">
      <p class="practitioner__name">Marcus Thelwick</p>
      <p class="practitioner__role">Acupuncturist Member KPTG</p>
      <p class="practitioner__role">BVF Treatment Provider</p>
    </div>
    <span class="divider"></span>

    <div class="contact">
      <p class="contact__row">
        <svg class="contact__icon" viewBox="0 0 24 24" aria-hidden="true">
          <circle cx="12" cy="12" r="11" fill="none" stroke="var(--muted-white)" stroke-width="1.6"/>
          <path d="M8 6.5l2 2.5-1.2 1.5c.8 1.6 2 2.8 3.7 3.7l1.5-1.2 2.5 2-1.2 2c-4.2-.3-8-4.1-8.3-8.3z" fill="var(--muted-white)"/>
        </svg>
        <span>482 1358 · 027 514 3820</span>
      </p>
      <p class="contact__row">
        <svg class="contact__icon" viewBox="0 0 24 24" aria-hidden="true">
          <circle cx="12" cy="12" r="11" fill="none" stroke="var(--muted-white)" stroke-width="1.6"/>
          <rect x="6" y="8" width="12" height="8" fill="none" stroke="var(--muted-white)" stroke-width="1.4"/>
          <path d="M6 8l6 5 6-5" fill="none" stroke="var(--muted-white)" stroke-width="1.4"/>
        </svg>
        <span>marcus@swpath.example.nz</span>
      </p>
    </div>
  </section>

</main>
</body>
</html>
```